Wordpress Web Design & Coding for velnoragroup.ca

We need a website for a new investment company that is visually grabbing and vibrant. We would like to see a web page that displays trust, growth and confidence. Needs to be responsive and mobile friendly for all browsers and coded for both Android & IOS.

Open to the number of pages and menu items. I selected 4 but if you feel the layout would work better with less I am open to this. Need to sell the people (management team/related businesses) and then show where the invested money will be going (upcoming projects).

Company Info:

Velnora is an investment company put together by a group of seasoned business professionals who have come together to combine decades of success in the real estate development, management, financing and medical services. The company will be a full service company offering turn key solutions for medical professionals.

Vel-Nora will focus on providing a full range of services via a group of distinct companies to deliver newly emerging needs of the medical community. The end goal will be to create complete solutions for individuals in the medical community. Our group has experience and success with the conceptualization, construction and financing of medical and dental clinic spaces. Vel-Nora Group will be established to accommodate all areas of the development and creation of clinics for medical professionals from building construction to equipment financing and administrations.

You can mention these companies and take photos from their websites. You can also use stock photos.

Our construction partner:
https://382bld.com/projects/

Our equipment leasing partner:
https://www.pordiva.com/

Our Management Team and medical partners

Gil Parkes
https://www.mysoundpoise.ca/

Milos Vendraker
https://www.qrtdentalservices.com/about-us

PROPOSED PROJECTS (see attachment for details)
Hollowmere Business Park
Cresfield Business Park
Mt. Corwin Ridge Professional

Investors

Investment

Sans Serif

Must have
• Wordpress – must be both desktop and mobile friendly with fast page load speed
Ability to edit after ourselves in Wordpress
Attractive home page with logo etc.
Logo colours are: for the blue the pantone color is #0355a3
and for the green is #8cc63f

Sections, about us, what we do/services we provide, contact us

```html
<!DOCTYPE html>
<html lang="en">
<head>
<meta charset="utf-8">
<title>Vel-Nora Group</title>
<link href="https://fonts.googleapis.com/css2?family=Arimo:wght@400;700&family=Lato:wght@400;700&display=swap" rel="stylesheet">
<style>
:root{
  --blue:#0355a3;--green:#8cc63f;--green-dark:#5faa2a;--ink:#333;--grey:#666;--line:#cfcfcf;--white:#fff;
}
*{box-sizing:border-box;margin:0;padding:0}
html,body{width:1200px;height:3194px;overflow:hidden;background:var(--white)}
body{position:relative;font-family:'Lato',sans-serif;color:var(--ink)}
.abs{position:absolute}
.topline{left:0;top:0;width:1200px;height:4px;background:var(--green)}
.brand{left:112px;top:40px;font:700 26px/1 'Lato',sans-serif;color:var(--blue);letter-spacing:.5px}
.brand small{display:block;font-size:13px;color:var(--green-dark);margin-top:5px;letter-spacing:2px;text-align:center}
.call{left:656px;top:22px;display:flex;align-items:center;gap:14px;font-size:14px}
.call .dot{width:36px;height:36px;border-radius:50%;background:var(--green);display:flex;align-items:center;justify-content:center}
.call b{font-size:21px;font-weight:400}
.login{left:985px;top:21px;width:102px;height:35px;border-radius:18px;background:var(--green);color:var(--white);font-size:14px;font-weight:700;display:flex;align-items:center;justify-content:center}
.nav{top:76px;font-size:15px;color:var(--ink)}
.nav.active{color:var(--blue)}
.hero-box{left:112px;top:283px;width:524px;height:281px;background:rgba(120,128,138,.72);padding:24px 0 0 45px;color:var(--white)}
.hero-box h1{font:700 55px/58px 'Arimo',sans-serif}
.hero-box p{font:700 14px/26px 'Arimo',sans-serif;margin-top:12px;width:450px}
.btn{display:flex;align-items:center;justify-content:center;color:var(--white);background:linear-gradient(#8fd143,#5fb32e);font-weight:700;font-size:15px;border-radius:22px}
.dots span{display:block;width:12px;height:12px;border-radius:50%;background:var(--white);margin-bottom:13px}
.dots span:first-child{background:var(--green)}
.about h2{font:700 36px/1 'Arimo',sans-serif;color:var(--blue)}
.about h2 em{font-style:normal;color:var(--green)}
.about p{margin-top:34px;width:495px;font:14px/25.7px 'Arimo',sans-serif;color:var(--grey);text-align:justify}
.sec-title{width:1200px;text-align:center;font:700 35px/1 'Arimo',sans-serif;color:var(--white)}
.svc{width:440px;display:flex;color:var(--white)}
.svc .ico{width:95px;height:95px;flex:none}
.svc .bar{width:2px;height:100px;background:var(--white);margin:0 20px 0 16px;flex:none}
.svc h3{font:700 21px/1 'Arimo',sans-serif;margin-top:2px}
.svc p{font:13.5px/26px 'Arimo',sans-serif;margin-top:6px;width:320px}
.touch{width:1200px;text-align:center;font:700 31px/1 'Lato',sans-serif;color:var(--blue)}
.touch em{font-style:normal;color:var(--green)}
.field{border:1px solid var(--line);background:var(--white);font-size:14px;color:var(--grey);padding:22px 18px}
.submit{left:460px;top:2544px;width:280px;height:58px;background:linear-gradient(#8fd143,#5fb32e);color:var(--white);font-size:19px;font-weight:700;letter-spacing:5px;display:flex;align-items:center;justify-content:center}
.captcha{left:762px;top:2553px;width:170px;height:41px;border:1px solid #d3d3d3;background:#f9f9f9;font-size:9px;display:flex;align-items:center;gap:8px;padding-left:10px}
.captcha i{width:15px;height:15px;border:2px solid #c1c1c1;background:var(--white)}
.foot h4{font:700 20px/1 'Lato',sans-serif;color:var(--white)}
.foot ul{list-style:none;margin-top:24px}
.foot li{font-size:15px;color:var(--white);height:31px;display:flex;align-items:center;gap:12px}
.foot p{font-size:15px;color:var(--white)}
.social{width:40px;height:40px;border-radius:50%;background:var(--white)}
</style>
</head>
<body>
<div class="abs topline"></div>
<div class="abs brand">VEL-NORA<small>GROUP</small></div>
<div class="abs call"><span class="dot"><svg width="16" height="16" viewBox="0 0 24 24"><path fill="#fff" d="M6.6 10.8a15 15 0 006.6 6.6l2.2-2.2c.3-.3.7-.4 1-.2 1.1.4 2.3.6 3.6.6.6 0 1 .4 1 1V20c0 .6-.4 1-1 1A17 17 0 013 4c0-.6.4-1 1-1h3.5c.6 0 1 .4 1 1 0 1.3.2 2.5.6 3.6.1.3 0 .7-.2 1z"/></svg></span><span>Call us Today : <b>+1 888 888 8888</b></span></div>
<div class="abs login">&#9711;&nbsp;Login</div>
<svg class="abs" style="left:366px;top:55px" width="26" height="18"><path d="M2 9l7 6L24 2" stroke="#8cc63f" stroke-width="3" fill="none"/></svg>
<div class="abs nav active" style="left:356px">Home</div>
<div class="abs nav" style="left:423px">About us</div>
<div class="abs nav" style="left:508px">Services</div>
<div class="abs nav" style="left:591px">Our construction partner</div>
<div class="abs nav" style="left:783px">Leasing partner</div>
<div class="abs nav" style="left:912px">Team</div>
<div class="abs nav" style="left:975px">Contact us</div>
<svg class="abs" style="left:1073px;top:78px" width="15" height="15"><circle cx="6" cy="6" r="4.5" stroke="#333" stroke-width="2" fill="none"/><path d="M9.5 9.5L14 14" stroke="#333" stroke-width="2"/></svg>

<svg class="abs" style="left:0;top:0" width="1200" height="3194">
  <defs>
    <linearGradient id="heroFill" x1="0" y1="0" x2="1" y2="0.6"><stop offset="0" stop-color="#c4d8e6"/><stop offset=".5" stop-color="#6f94b4"/><stop offset="1" stop-color="#1c2f4a"/></linearGradient>
    <linearGradient id="band" x1="0" y1="0" x2="1" y2="0"><stop offset="0" stop-color="#b5dd70"/><stop offset="1" stop-color="#5fa82a"/></linearGradient>
  </defs>
  <polygon points="40,660 283,826 1010,668 283,793" fill="url(#band)"/>
  <polygon role="img" aria-label="Businessman holding a tablet with rising financial charts" points="0,115 1200,115 1200,601 283,793 0,645" fill="url(#heroFill)"/>
  <polygon points="250,1438 917,1310 1160,1455 917,1334" fill="url(#band)"/>
  <polygon points="30,1945 283,2093 1010,1952 283,2064" fill="url(#band)"/>
  <polygon points="0,1444 917,1330 1200,1469 1200,1934 283,2064 0,1934" fill="var(--blue)"/>
  <polygon points="150,2862 917,2683 1165,2873 917,2708" fill="url(#band)"/>
  <polygon points="0,2873 917,2708 1200,2880 1200,3194 0,3194" fill="var(--blue)"/>
  <g role="img" aria-label="Collage of business and medical team photos">
    <rect x="642" y="872" width="161" height="132" fill="#a89480"/>
    <rect x="808" y="912" width="95" height="96" fill="#b9b6b0"/>
    <rect x="908" y="915" width="109" height="88" fill="var(--blue)"/>
    <rect x="702" y="1009" width="198" height="94" fill="#4f5a63"/>
    <rect x="906" y="1009" width="103" height="94" fill="#d8d2c8"/>
    <rect x="694" y="1108" width="110" height="88" fill="var(--blue)"/>
    <rect x="808" y="1108" width="95" height="106" fill="#6b6e74"/>
    <rect x="908" y="1108" width="160" height="131" fill="#7d6f62"/>
  </g>
</svg>

<div class="abs hero-box"><h1>VEL-NORA<br>SOLUTION</h1><p>Lorem ipsum dolor sit amet, consectetur adipiscing elit, sed do eiusmod tempor incididunt ut labore et dolore magna aliqua.</p></div>
<div class="abs btn" style="left:157px;top:488px;width:137px;height:41px;font-size:14px">GET STARTED</div>
<div class="abs dots" style="left:1141px;top:372px"><span></span><span></span><span></span></div>

<section class="abs about" style="left:95px;top:924px">
  <h2>ABOUT <em>VELNORA SOLUTIONS</em></h2>
  <svg width="64" height="4" style="display:block;margin-top:22px"><rect width="64" height="3" fill="#0355a3"/></svg>
  <p style="margin-top:10px">Lorem ipsum dolor sit amet, consectetur adipiscing elit, sed do eiusmod tempor incididunt ut labore et dolore magna aliqua. Ut enim ad minim veniam, quis nostrud exercitation ullamco laboris nisi ut aliquip ex ea commodo consequat.Lorem ipsum dolor sit amet, consectetur adipiscing elit, sed do eiusmod tempor incididunt ut labore et dolore magna aliqua. Ut enim ad minim veniam, quis nostrud exercitation ullamco laboris nisi ut aliquip ex ea commodo consequat.</p>
</section>
<div class="abs btn" style="left:95px;top:1184px;width:136px;height:40px;font-size:14px">LEARN MORE</div>

<h2 class="abs sec-title" style="left:0;top:1499px">SERVICES WE PROVIDE</h2>
<div class="abs" style="left:568px;top:1546px;width:64px;height:3px;background:#fff"></div>

<div class="abs svc" style="left:118px;top:1602px">
  <svg class="ico" viewBox="0 0 95 95" fill="none" stroke="#fff" stroke-width="3"><circle cx="47" cy="47" r="36" stroke-dasharray="12 6"/><circle cx="47" cy="47" r="26"/><path d="M33 50l14-12 14 12M37 47v13h20V47M44 60v-7h6v7"/></svg>
  <span class="bar"></span><div><h3>Real estate development</h3><p>Lorem ipsum dolor sit amet, consectetur adipis cing elit, sed do eiusmod tempor incididunt ut labore et dolore magna aliqua.</p></div>
</div>
<div class="abs svc" style="left:600px;top:1602px">
  <svg class="ico" viewBox="0 0 95 95" fill="none" stroke="#fff" stroke-width="3"><rect x="17" y="10" width="54" height="70" rx="4"/><path d="M25 28h8M38 28h22M25 42h8M38 42h18M25 56h8M38 56h12"/><circle cx="66" cy="68" r="15" fill="#0355a3"/><path d="M59 68l5 5 9-10"/></svg>
  <span class="bar"></span><div><h3>Management</h3><p>Lorem ipsum dolor sit amet, consectetur adipis cing elit, sed do eiusmod tempor incididunt ut labore et dolore magna aliqua.</p></div>
</div>
<div class="abs svc" style="left:118px;top:1782px">
  <svg class="ico" viewBox="0 0 95 95" fill="none" stroke="#fff" stroke-width="3"><rect x="4" y="8" width="26" height="18" rx="3"/><circle cx="78" cy="18" r="12"/><circle cx="45" cy="32" r="9"/><path d="M30 55c2-10 28-10 30 0"/><circle cx="50" cy="72" r="12" stroke-dasharray="6 4"/><rect x="68" y="65" width="22" height="16" rx="2"/><path d="M8 72c0-6 10-6 8 2-2 3-4 3-4 7M12 88v1"/></svg>
  <span class="bar"></span><div><h3>Financing Services</h3><p>Lorem ipsum dolor sit amet, consectetur adipis cing elit, sed do eiusmod tempor incididunt ut labore et dolore magna aliqua.</p></div>
</div>
<div class="abs svc" style="left:600px;top:1782px">
  <svg class="ico" viewBox="0 0 95 95" fill="none" stroke="#fff" stroke-width="3"><rect x="26" y="4" width="46" height="86" rx="5"/><path d="M26 16h46M26 78h46"/><path d="M37 46c0-14 24-14 24 0"/><rect x="33" y="44" width="7" height="12" rx="2"/><rect x="58" y="44" width="7" height="12" rx="2"/><rect x="40" y="58" width="16" height="13"/></svg>
  <span class="bar"></span><div><h3>Medical services</h3><p>Lorem ipsum dolor sit amet, consectetur adipis cing elit, sed do eiusmod tempor incididunt ut labore et dolore magna aliqua.</p></div>
</div>

<h2 class="abs touch" style="left:0;top:2183px">GET <em>IN TOUCH</em></h2>
<div class="abs field" style="left:188px;top:2235px;width:403px;height:61px">Name</div>
<div class="abs field" style="left:608px;top:2235px;width:403px;height:61px">Email</div>
<div class="abs field" style="left:188px;top:2312px;width:403px;height:61px">Number</div>
<div class="abs field" style="left:608px;top:2312px;width:403px;height:61px">Subject</div>
<div class="abs field" style="left:188px;top:2389px;width:824px;height:137px">What can we help you with?</div>
<div class="abs submit">SUBMIT</div>
<div class="abs captcha"><i></i>I'm not a robot</div>

<div class="abs foot" style="left:109px;top:2925px">
  <h4>QUICK LINKS</h4>
  <ul><li>&raquo; Home</li><li>&raquo; About us</li><li>&raquo; Services</li><li>&raquo; Contact us</li><li>&raquo; Privacy policy</li></ul>
</div>
<div class="abs foot" style="left:403px;top:2925px">
  <h4>CONTACT US</h4>
  <ul>
    <li style="align-items:flex-start;height:62px;line-height:31px"><svg width="10" height="14" style="margin-top:8px;flex:none"><path d="M5 0a5 5 0 015 5c0 4-5 9-5 9S0 9 0 5a5 5 0 015-5z" fill="#fff"/></svg><span style="margin-left:12px">Lorem ipsum dolor sit amet,<br>consectetur adipiscing</span></li>
    <li><svg width="12" height="12" viewBox="0 0 24 24"><path fill="#fff" d="M6.6 10.8a15 15 0 006.6 6.6l2.2-2.2c.3-.3.7-.4 1-.2 1.1.4 2.3.6 3.6.6.6 0 1 .4 1 1V20c0 .6-.4 1-1 1A17 17 0 013 4c0-.6.4-1 1-1h3.5c.6 0 1 .4 1 1 0 1.3.2 2.5.6 3.6.1.3 0 .7-.2 1z"/></svg><span style="margin-left:8px">+1 888 888 8888</span></li>
    <li><svg width="14" height="10"><rect width="14" height="10" fill="#fff"/><path d="M0 0l7 5 7-5" stroke="#0355a3" fill="none"/></svg><span style="margin-left:6px">info@velnoragroup.com</span></li>
  </ul>
</div>
<div class="abs foot" style="left:748px;top:2925px">
  <h4>SUBSCRIBE THE NEWSLETTER</h4>
  <p style="margin-top:28px">Lorem ipsum dolor sit amet, consectetur adipiscing</p>
</div>
<div class="abs field" style="left:751px;top:3007px;width:247px;height:43px;padding:12px 24px;border:none">Email Address</div>
<div class="abs" style="left:751px;top:3063px;width:118px;height:42px;background:var(--green);color:#fff;font-weight:700;font-size:14px;display:flex;align-items:center;justify-content:center">SUBSCRIBE</div>
<p class="abs" style="left:109px;top:3142px;font-size:15px;color:#fff">&copy; Copyrights 2020 | Velnora Solutions</p>
<div class="abs social" style="left:961px;top:3121px"></div>
<div class="abs social" style="left:1004px;top:3121px"></div>
<div class="abs social" style="left:1048px;top:3121px"></div>
</body>
</html>
```